Bright Harbor Counseling Letterhead for hip modern business

I would like some ombre use of the colors in the logo hip letterhead that incorporates logo colors and feel, needs to connect with young professionals and college students. i need to be able to write letters to schools to excuse absences as well. i like color blocks on one side preferably using colors from the attached logo design.

Target Market(s)

high income young people, young adults and college students

Industry/Entity Type

mental health

Font styles to use
Serif
Sans Serif

Colors
0054AA
0677BA
7BADD7
CADEEF
E8F1F8
0094D4
00A9DD
6FCCEA
C7EBF8
E9F6FB
00AB8E
00BBA5
67D7C9
C6EFE9
E9F9F6
59FF00
82FF00
B8FF75
E3FFCB
F4FFEA
A7469A
B969AE
D3A5CF
EDDBEB
F8F0F9
6B429C
8869AF
B7A5CE
E3DAEB
F3F0F8

Requirements
Must have
• a modern hip feel, somewhat color

```html
<!DOCTYPE html>
<html lang="en">
<head>
<meta charset="utf-8">
<title>Bright Harbor Counseling Letterhead</title>
<link rel="stylesheet" href="https://fonts.googleapis.com/css2?family=Jost:wght@300;400&display=swap">
<style>
  :root {
    --backdrop: #8a6c55;
    --paper: #ffffff;
    --ink: #1a1a1a;
    --teal: #00bba5;
    --sky: #0094d4;
    --blue: #0677ba;
    --violet: #8869af;
    --plum: #a7469a;
    --rose: #b9507f;
  }
  * { margin: 0; padding: 0; box-sizing: border-box; }
  html, body {
    width: 1200px;
    height: 900px;
    overflow: hidden;
    background: var(--backdrop);
  }
  .canvas {
    position: relative;
    width: 1200px;
    height: 900px;
  }
  .letterhead {
    position: absolute;
    left: 283px;
    top: 40px;
    width: 634px;
    height: 820px;
    background: var(--paper);
    box-shadow: 0 4px 14px rgba(0, 0, 0, 0.28);
    overflow: hidden;
    font-family: "Jost", "Futura", sans-serif;
    color: var(--ink);
  }
  .brand {
    position: absolute;
    right: 200px;
    top: 72px;
    display: flex;
    align-items: flex-start;
    gap: 8px;
  }
  .brand-name {
    text-align: right;
    font-weight: 300;
    color: var(--ink);
  }
  .brand-name .primary {
    display: block;
    font-size: 31px;
    line-height: 1;
    letter-spacing: 0.01em;
  }
  .brand-name .secondary {
    display: block;
    font-size: 16px;
    line-height: 1.3;
    letter-spacing: 0.16em;
    margin-top: 4px;
  }
  .brand-dot {
    width: 14px;
    height: 14px;
    border-radius: 50%;
    background: var(--teal);
    margin-top: 2px;
  }
  .color-block {
    position: absolute;
    left: 0;
    bottom: 0;
    width: 176px;
    height: 140px;
    border-top-right-radius: 120px 100px;
    background: linear-gradient(60deg, var(--violet) 0%, var(--blue) 38%, var(--sky) 55%, var(--plum) 78%, var(--rose) 100%);
    opacity: 0.85;
  }
  .contact {
    position: absolute;
    right: 28px;
    bottom: 27px;
    list-style: none;
    text-align: right;
    font-size: 10.5px;
    font-weight: 400;
    letter-spacing: 0.1em;
    line-height: 19.5px;
  }
</style>
</head>
<body>
  <main class="canvas">
    <article class="letterhead">
      <header class="brand">
        <div class="brand-name">
          <span class="primary">Bright Harbor</span>
          <span class="secondary">Counseling</span>
        </div>
        <span class="brand-dot" aria-hidden="true"></span>
      </header>

      <div class="color-block" role="img" aria-label="Decorative cluster of overlapping translucent colour circles in teal, blue, purple and magenta"></div>

      <ul class="contact">
        <li>+41 78 555 0142</li>
        <li>info@brightharbor.com</li>
        <li>www.brightharbor.com</li>
      </ul>
    </article>
  </main>
</body>
</html>
```